Company Proposal Powerpoint Template

We would like to update our overall proposal presentation with a fresh, new look that might appeal to the younger generation. We are a full-meeting management company that specializes in corporate events sales meetings, incentive trips, and tradeshows/conferences.
We have a core set of slides that we use for presentations, but will also need to customize based on the customers we service and what we are selling each potential client.
We have a Orbis Meetings, but we are not tied into the colors schemes for the logo and are okay adding the logo in black or white versus in color.
I have included our current look and feel for this presentation. This will also give you content that we typically add to this presentation.
Reason: Traveling out of the office so limited access to review the art.
Industry/Entity Type
It Company
Look and feel
Each slider illustrates characteristics of the customer's brand and the style your logo design should communicate.

```html
<!DOCTYPE html>
<html lang="en">
<head>
<meta charset="utf-8">
<title>Company Proposal Template</title>
<link href="https://fonts.googleapis.com/css2?family=Montserrat:wght@400;600;700&family=Open+Sans:wght@400;600&display=swap" rel="stylesheet">
<style>
:root{
  --pink:#d81f4f;
  --blue:#1ba4dc;
  --navy:#1f3f5b;
  --ink:#4a4a4a;
  --muted:#9a9a9a;
  --line:#e4e4e4;
  --bg:#ffffff;
  --page:#f2f2f2;
}
*{box-sizing:border-box;margin:0;padding:0}
html,body{width:809px;height:1200px;overflow:hidden;background:var(--page)}
body{font-family:"Open Sans",Arial,sans-serif;color:var(--ink)}
.deck{width:809px;height:1200px;display:grid;grid-template-columns:repeat(3,1fr);grid-template-rows:repeat(6,1fr);gap:4px 5px}
.slide{position:relative;background:var(--bg);overflow:hidden;box-shadow:0 0 0 1px var(--line)}
.slide::after{content:"";position:absolute;left:0;right:0;bottom:0;height:7px;background:linear-gradient(90deg,var(--pink) 0 22%,var(--blue) 22% 100%)}
.photo{position:absolute;background:linear-gradient(135deg,#cfd6de,#8e9aa8)}
.photo.warm{background:linear-gradient(135deg,#e8d8c8,#9c7a5e)}
.photo.cool{background:linear-gradient(135deg,#dbe6ef,#7f98b0)}
.photo.dark{background:linear-gradient(135deg,#6b5a4c,#2e2621)}
.brand{position:absolute;top:8px;right:10px;display:flex;align-items:center;gap:3px;font-family:"Montserrat",sans-serif;font-weight:600;font-size:6px;color:var(--navy)}
.brand i{width:9px;height:9px;border-radius:50%;background:var(--pink);display:block}
.title{position:absolute;font-family:"Montserrat",sans-serif;font-weight:700;font-size:11px;line-height:1.15;color:var(--pink)}
.title.blue{color:var(--blue)}
.title.white{color:#fff}
.rule{display:block;width:24px;height:2px;background:var(--blue);margin-top:4px}
.copy{position:absolute;font-size:4.6px;line-height:1.45;color:var(--muted)}
.copy b{color:var(--ink);font-weight:600}
.list{position:absolute;list-style:none}
.list li{display:flex;align-items:flex-start;gap:4px;margin-bottom:7px;font-size:4.6px;line-height:1.4;color:var(--muted)}
.list li::before{content:"";flex:none;width:8px;height:8px;border-radius:50%;background:var(--pink)}
.list.blue li::before{background:var(--blue)}
.list li b{display:block;color:var(--ink);font-size:5px}
.band{position:absolute;background:var(--pink)}
.band.blue{background:var(--blue)}
.lead{font-family:"Montserrat",sans-serif;font-weight:700;font-size:7px;color:var(--ink);line-height:1.2}
.lead span{color:var(--pink)}
.step{position:absolute;font-size:4.4px;text-align:center;color:var(--muted);width:36px}
.step b{display:block;color:var(--ink);font-size:5px}
</style>
</head>
<body>
<main class="deck">

  <!-- 1 Registration Services -->
  <section class="slide">
    <div class="photo cool" style="left:0;top:0;width:100%;height:72%" role="img" aria-label="Photo of a smiling support agent wearing a headset"></div>
    <div class="brand"><i></i>Orbis Meetings</div>
    <div class="band" style="left:0;top:62%;width:100%;height:28px"></div>
    <div class="band blue" style="left:0;top:62%;width:14px;height:28px"></div>
    <h2 class="title white" style="left:80px;top:131px;font-size:10px">Registration Services</h2>
  </section>

  <!-- 2 Website Development -->
  <section class="slide">
    <div class="band" style="left:0;top:0;width:30%;height:100%"></div>
    <div class="photo" style="left:0;top:0;width:30%;height:48%" role="img" aria-label="Photo of a laptop on a desk"></div>
    <h2 class="title" style="left:100px;top:12px">Website<br>Development</h2>
    <ul class="list" style="left:100px;top:48px;width:150px">
      <li><span><b>Custom event websites</b>Branded pages built for each client event.</span></li>
      <li><span><b>Mobile friendly</b>Layouts that work on every screen size.</span></li>
      <li><span><b>Easy updates</b>Content changes handled by our team fast.</span></li>
    </ul>
  </section>

  <!-- 3 Data management & call center -->
  <section class="slide">
    <div class="photo cool" style="left:0;top:0;width:40%;height:100%" role="img" aria-label="Photo of a call center agent with a headset"></div>
    <h2 class="title" style="left:118px;top:12px">Data management<br>&amp; call center</h2>
    <ul class="list blue" style="left:118px;top:50px;width:135px">
      <li><span><b>Attendee database</b>Secure records for every guest.</span></li>
      <li><span><b>Live call support</b>Friendly help during registration.</span></li>
      <li><span><b>Reporting</b>Clear daily updates for your team.</span></li>
    </ul>
  </section>

  <!-- 4 Online Registration -->
  <section class="slide">
    <div style="position:absolute;left:14px;top:40px;display:flex;align-items:center;gap:4px;font-family:'Montserrat',sans-serif;font-weight:700;font-size:14px;color:var(--pink)"><span style="width:22px;height:22px;border-radius:50%;background:var(--pink);display:block"></span>Regiflow</div>
    <div style="position:absolute;left:14px;top:150px;width:40px;height:12px;background:var(--line)"></div>
    <div style="position:absolute;left:60px;top:150px;width:40px;height:12px;background:var(--line)"></div>
    <h2 class="title" style="left:130px;top:12px">Online<br>Registration</h2>
    <ul class="list" style="left:130px;top:48px;width:125px">
      <li><span><b>Fast sign up</b>Guests register in a few simple steps.</span></li>
      <li><span><b>Secure payments</b>Fees collected safely online.</span></li>
      <li><span><b>Live tracking</b>See counts as they come in.</span></li>
    </ul>
  </section>

  <!-- 5 Air Ticketing -->
  <section class="slide">
    <div class="photo cool" style="left:0;top:0;width:100%;height:40%" role="img" aria-label="Photo of an airplane wing in the sky"></div>
    <h2 class="title" style="left:12px;top:88px">Air Ticketing<br>Service</h2>
    <p class="copy" style="left:110px;top:88px;width:145px">We book group and individual flights for every attendee, manage changes and keep costs on budget so your travellers arrive on time and ready for the meeting ahead.</p>
  </section>

  <!-- 6 Portfolio Page -->
  <section class="slide">
    <div class="photo warm" style="left:0;top:0;width:44%;height:100%" role="img" aria-label="Photo of a conference hall with guests"></div>
    <h2 class="title" style="left:128px;top:12px">Portfolio Page</h2>
    <p class="copy" style="left:128px;top:32px;width:125px"><b>Meetings that matter</b><br>A look at recent events we planned for clients.</p>
    <div class="photo dark" style="left:128px;top:76px;width:125px;height:100px" role="img" aria-label="Photo of a dinner event setting"></div>
  </section>

  <!-- 7 About Us -->
  <section class="slide">
    <div class="photo warm" style="left:0;top:20px;width:44%;height:170px" role="img" aria-label="Portrait photo of a businesswoman"></div>
    <h2 class="title" style="left:10px;top:6px;font-size:9px">About Us</h2>
    <div class="lead" style="position:absolute;left:128px;top:36px;width:128px">We are <span>Orbis Meetings</span><br>Taking Services to a New Level of Excellence</div>
    <p class="copy" style="left:128px;top:72px;width:128px">We are a full meeting management company for corporate events, sales meetings, incentive trips and trade shows. Our team plans each detail with care.</p>
  </section>

  <!-- 8 One Vision & Mission -->
  <section class="slide">
    <h2 class="title blue" style="left:12px;top:10px">One Vision &amp; Mission</h2>
    <div class="band blue" style="left:12px;top:34px;width:120px;height:140px"></div>
    <p class="copy" style="left:20px;top:44px;width:104px;color:#fff"><b style="color:#fff">Our Vision</b><br>To be the first choice for memorable business events.</p>
    <div class="photo" style="left:136px;top:34px;width:120px;height:70px" role="img" aria-label="Photo of a team meeting"></div>
    <p class="copy" style="left:136px;top:110px;width:118px"><b>Our Mission</b><br>Deliver smooth, creative meetings that leave every guest inspired.</p>
  </section>

  <!-- 9 Our Services -->
  <section class="slide">
    <h2 class="title blue" style="left:12px;top:10px">Our Services</h2>
    <div class="photo warm" style="left:12px;top:32px;width:60px;height:40px" role="img" aria-label="Photo of event staff"></div>
    <div class="photo" style="left:76px;top:32px;width:60px;height:40px" role="img" aria-label="Photo of a business meeting"></div>
    <p class="copy" style="left:12px;top:80px;width:125px"><b>Event planning</b><br>Venues, agendas and guest care.</p>
    <ul class="list" style="left:150px;top:32px;width:105px">
      <li><span><b>Incentive trips</b>Rewards that travel.</span></li>
      <li><span><b>Trade shows</b>Booths and logistics.</span></li>
      <li><span><b>Conferences</b>Full event support.</span></li>
    </ul>
  </section>

  <!-- 10 One Expertise -->
  <section class="slide">
    <div class="brand" style="left:10px;right:auto"><i></i>Orbis Meetings</div>
    <h2 class="title blue" style="left:12px;top:30px">One Expertise</h2>
    <ul class="list blue" style="left:12px;top:54px;width:110px">
      <li><span><b>Sales meetings</b>Focused and on time.</span></li>
      <li><span><b>Corporate events</b>Polished and branded.</span></li>
      <li><span><b>Group travel</b>Simple and safe.</span></li>
    </ul>
    <div class="photo cool" style="left:130px;top:0;width:136px;height:100%" role="img" aria-label="Photo of a modern office building"></div>
  </section>

  <!-- 11 Your Title Goes Here -->
  <section class="slide">
    <h2 class="title blue" style="left:12px;top:10px">Your Title Goes Here</h2>
    <div class="band" style="left:12px;top:34px;width:80px;height:64px"></div>
    <p class="copy" style="left:18px;top:42px;width:68px;color:#fff">Add a short point about your service here.</p>
    <div class="photo warm" style="left:96px;top:34px;width:80px;height:64px" role="img" aria-label="Photo of a seated audience"></div>
    <div class="band blue" style="left:180px;top:34px;width:76px;height:64px"></div>
    <div class="photo" style="left:12px;top:102px;width:80px;height:74px" role="img" aria-label="Photo of a presenter"></div>
    <p class="copy" style="left:100px;top:108px;width:150px">Use this area to explain a key benefit in one or two short lines of text.</p>
  </section>

  <!-- 12 Quote Area -->
  <section class="slide">
    <h2 class="title blue" style="left:12px;top:10px">Quote Area</h2>
    <div class="band blue" style="left:12px;top:34px;width:110px;height:80px"></div>
    <p class="copy" style="left:20px;top:44px;width:96px;color:#fff;font-size:5.4px">&ldquo;A great meeting is planned with care, so every guest feels welcome.&rdquo;</p>
    <div class="photo dark" style="left:128px;top:34px;width:128px;height:142px" role="img" aria-label="Photo of a banquet hall"></div>
    <p class="copy" style="left:12px;top:122px;width:110px">Share a favourite client quote or company value in this space.</p>
  </section>

  <!-- 13 Text Area -->
  <section class="slide">
    <h2 class="title" style="left:12px;top:10px">Text Area</h2>
    <div class="lead" style="position:absolute;left:12px;top:32px;width:120px">We are <span>Orbis Meetings</span><br>Taking Services to a New Level of Excellence</div>
    <p class="copy" style="left:12px;top:68px;width:120px">Our planners handle every step, from the first site visit to the final thank you note, so your team can focus on results.</p>
    <div class="photo warm" style="left:142px;top:0;width:124px;height:100%" role="img" aria-label="Photo of a hotel lobby"></div>
  </section>

  <!-- 14 Text Area photo -->
  <section class="slide">
    <div class="photo warm" style="left:0;top:0;width:100%;height:58%" role="img" aria-label="Photo of two colleagues talking"></div>
    <div class="band blue" style="left:150px;top:20px;width:104px;height:90px"></div>
    <h2 class="title white" style="left:158px;top:28px;font-size:9px">Text Area</h2>
    <p class="copy" style="left:158px;top:46px;width:90px;color:#fff">A short note about your team and how you help clients succeed.</p>
    <p class="copy" style="left:12px;top:124px;width:240px">Write supporting details here, such as key figures or the number of events planned last year.</p>
  </section>

  <!-- 15 Text Area -->
  <section class="slide">
    <h2 class="title" style="left:12px;top:10px">Text Area</h2>
    <div class="photo dark" style="left:12px;top:32px;width:120px;height:70px" role="img" aria-label="Photo of a conference room"></div>
    <p class="copy" style="left:140px;top:32px;width:116px">We create events that connect people and ideas. Each plan is shaped to the goals of our client.</p>
    <p class="copy" style="left:12px;top:110px;width:244px">From small board meetings to large conferences, our team brings the same care and attention to detail every time.</p>
  </section>

  <!-- 16 We are -->
  <section class="slide">
    <div class="band" style="left:0;top:0;width:100%;height:56%"></div>
    <div class="lead" style="position:absolute;left:12px;top:14px;width:120px;color:#fff">We are Orbis Meetings<br>Taking Services to a New Level of Excellence</div>
    <ul class="list blue" style="left:140px;top:14px;width:115px">
      <li style="color:#fff"><span><b style="color:#fff">Planning</b>Clear timelines.</span></li>
      <li style="color:#fff"><span><b style="color:#fff">Travel</b>Smooth arrivals.</span></li>
      <li style="color:#fff"><span><b style="color:#fff">Support</b>On site staff.</span></li>
    </ul>
    <div class="photo warm" style="left:12px;top:80px;width:110px;height:100px" role="img" aria-label="Portrait photo of a smiling businesswoman"></div>
  </section>

  <!-- 17 Workflow Area -->
  <section class="slide">
    <h2 class="title blue" style="left:12px;top:10px">Workflow Area</h2>
    <svg style="position:absolute;left:12px;top:56px" width="242" height="60" viewBox="0 0 242 60" aria-hidden="true">
      <path d="M10 30 Q40 0 70 30 T130 30 T190 30 T240 30" fill="none" stroke="var(--blue)" stroke-width="4"/>
      <path d="M10 30 Q40 60 70 30" fill="none" stroke="var(--pink)" stroke-width="4"/>
      <circle cx="20" cy="30" r="9" fill="var(--pink)"/>
      <circle cx="70" cy="30" r="9" fill="var(--blue)"/>
      <circle cx="120" cy="30" r="9" fill="var(--pink)"/>
      <circle cx="170" cy="30" r="9" fill="var(--blue)"/>
      <circle cx="220" cy="30" r="9" fill="var(--pink)"/>
    </svg>
    <div class="step" style="left:14px;top:124px"><b>Step 1</b>Brief</div>
    <div class="step" style="left:64px;top:124px"><b>Step 2</b>Plan</div>
    <div class="step" style="left:114px;top:124px"><b>Step 3</b>Book</div>
    <div class="step" style="left:164px;top:124px"><b>Step 4</b>Host</div>
    <div class="step" style="left:214px;top:124px"><b>Step 5</b>Review</div>
  </section>

  <!-- 18 Portfolio Area -->
  <section class="slide">
    <h2 class="title" style="left:12px;top:10px">Portfolio Area</h2>
    <p class="copy" style="left:12px;top:32px;width:105px">Highlights from trade shows and conferences our team delivered this year.</p>
    <ul class="list" style="left:12px;top:70px;width:105px">
      <li><span><b>Tech summit</b>1,200 guests.</span></li>
      <li><span><b>Sales kickoff</b>Three cities.</span></li>
    </ul>
    <div class="photo dark" style="left:126px;top:32px;width:130px;height:144px" role="img" aria-label="Photo of a full conference auditorium"></div>
  </section>

</main>
</body>
</html>
```